Postcard Design Project

Dental Practice Name: Brennock Hill Dental (logo)Phone Number (310-555-0147) Front and backAddress (7816 N. Marlowe Ave. Ste. C, Culver City, CA, 90230. (Back side only)General, Cosmetic, and Implant Dentistry Mention: Emergencies/Walk-ins Welcome, "Hablamos Espanol", Open Weekends Front Side:Promotions: 1. $75 New Patient Special including Exam, X-Rays, and Cleaning 2. Free Consultation 3. Accept all PPO Insurances Services: 1. Implant ($800) + Implant Crown/Abutment ($1200) -use photo of missing tooth 2. Clear Braces (starting at $2900) -use picture of alignora teeth, cut out everything else and just use the before and after of the alignora pictures 3. Whitening ($95) -use pic of whitened teeth 4. White fillings (starting at $95) -use pic of silver to white fillings) Back Side: 1. Picture of practice 2. picture of map with pin location 3. address and phone number

```html
<!DOCTYPE html>
<html lang="en">
<head>
<meta charset="utf-8">
<title>Brennock Hill Dental – Postcard Back</title>
<link href="https://fonts.googleapis.com/css2?family=Bebas+Neue&family=Open+Sans:wght@400;700&display=swap" rel="stylesheet">
<style>
  :root {
    --brand-blue: #176a98;
    --brand-blue-dark: #11577e;
    --paper: #ffffff;
    --ink: #1c1c1c;
    --line: #2a2a2a;
    --map-base-1: #eef0f2;
    --map-base-2: #dfe4e8;
    --photo-tone-1: #b9975a;
    --photo-tone-2: #6f7f4c;
  }
  html, body {
    margin: 0;
    padding: 0;
    width: 789px;
    height: 1200px;
    overflow: hidden;
    background: var(--paper);
  }
  .postcard {
    position: absolute;
    top: 0;
    left: 0;
    width: 1200px;
    height: 789px;
    transform-origin: 0 0;
    transform: translateY(1200px) rotate(-90deg);
    background: var(--paper);
    font-family: "Open Sans", Arial, sans-serif;
  }
  .info-panel {
    position: absolute;
    left: 0;
    top: 0;
    width: 593px;
    height: 789px;
    background: var(--brand-blue);
    color: var(--paper);
  }
  .practice-name {
    position: absolute;
    left: 28px;
    top: 42px;
    margin: 0;
    font-family: "Bebas Neue", "Arial Narrow", sans-serif;
    font-weight: 400;
    font-size: 37px;
    line-height: 30px;
    letter-spacing: 0.5px;
  }
  .intro {
    position: absolute;
    left: 28px;
    top: 124px;
    width: 535px;
    margin: 0;
    font-size: 14.6px;
    line-height: 22.5px;
  }
  .location-visual {
    position: absolute;
    left: 60px;
    top: 248px;
    width: 533px;
    height: 367px;
  }
  .contact {
    position: absolute;
    left: 28px;
    top: 618px;
  }
  .contact-label {
    margin: 0;
    font-size: 15px;
    line-height: 18px;
    letter-spacing: 0.3px;
  }
  .contact-phone {
    margin: 0;
    font-family: "Bebas Neue", "Arial Narrow", sans-serif;
    font-size: 52px;
    line-height: 46px;
    letter-spacing: 0.5px;
  }
  .contact-address {
    position: relative;
    margin: 8px 0 0;
    padding-left: 22px;
    font-size: 14.6px;
    line-height: 20px;
    text-transform: uppercase;
  }
  .contact-address svg {
    position: absolute;
    left: 0;
    top: 2px;
  }
  .mailing-side {
    position: absolute;
    left: 593px;
    top: 0;
    width: 607px;
    height: 789px;
  }
  .stamp-box {
    position: absolute;
    left: 377px;
    top: 81px;
    width: 164px;
    height: 206px;
    border: 3px solid var(--ink);
  }
  .address-line {
    position: absolute;
    left: 70px;
    width: 474px;
    height: 2px;
    background: var(--line);
  }
  .return-label {
    position: absolute;
    left: 77px;
    top: 702px;
    margin: 0;
    font-size: 13px;
    font-weight: 700;
    color: var(--ink);
  }
</style>
</head>
<body>
<div class="postcard">
  <section class="info-panel">
    <h1 class="practice-name">Brennock Hill<br>Dental</h1>
    <p class="intro">General, Cosmetic and Implant Dentistry for the whole family.<br>Emergencies and Walk-ins Welcome. ¡Hablamos Español!<br>Open Weekends for your convenience. New patients, ask about<br>our $75 exam, x-rays and cleaning. We accept all PPO insurances.</p>

    <svg class="location-visual" viewBox="0 0 533 367" xmlns="http://www.w3.org/2000/svg">
      <defs>
        <linearGradient id="mapTone" x1="0" y1="0" x2="1" y2="1">
          <stop offset="0" stop-color="var(--map-base-1)"/>
          <stop offset="1" stop-color="var(--map-base-2)"/>
        </linearGradient>
        <linearGradient id="photoTone" x1="0" y1="0" x2="1" y2="1">
          <stop offset="0" stop-color="#8c6a3e"/>
          <stop offset="0.5" stop-color="var(--photo-tone-1)"/>
          <stop offset="1" stop-color="var(--photo-tone-2)"/>
        </linearGradient>
        <clipPath id="photoClip">
          <circle cx="-220" cy="380" r="596"/>
        </clipPath>
      </defs>
      <rect class="map-area" role="img" aria-label="Street map of the practice neighborhood with location pin" width="533" height="367" fill="url(#mapTone)"/>
      <rect class="practice-photo" role="img" aria-label="Photo of the dental practice storefront" width="533" height="367" fill="url(#photoTone)" clip-path="url(#photoClip)"/>
      <circle cx="-220" cy="380" r="596" fill="none" stroke="var(--brand-blue)" stroke-width="6"/>
      <g class="map-pin" transform="translate(428 67)">
        <path d="M0 -22 C-12 -22 -18 -13 -18 -5 C-18 8 0 22 0 22 C0 22 18 8 18 -5 C18 -13 12 -22 0 -22 Z" fill="var(--brand-blue-dark)"/>
        <circle cx="0" cy="-5" r="6" fill="#ffffff"/>
      </g>
    </svg>

    <div class="contact">
      <p class="contact-label">CALL US TODAY</p>
      <p class="contact-phone">310-555-0147</p>
      <p class="contact-address">
        <svg width="14" height="18" viewBox="0 0 14 18" aria-hidden="true"><path d="M7 0 C3 0 0 3 0 7 C0 12 7 18 7 18 C7 18 14 12 14 7 C14 3 11 0 7 0 Z" fill="#ffffff"/><circle cx="7" cy="7" r="2.6" fill="var(--brand-blue)"/></svg>
        7816 N. Marlowe Ave. Ste. C,<br>Culver City, CA, 90230
      </p>
    </div>
  </section>

  <section class="mailing-side">
    <div class="stamp-box"></div>
    <div class="address-line" style="top:486px"></div>
    <div class="address-line" style="top:569px"></div>
    <div class="address-line" style="top:651px"></div>
    <p class="return-label">LOREM IPSUM</p>
  </section>
</div>
</body>
</html>
```